Harbor Business Cards

I need a business card designed with the following information.

Company Name: Harbor Wealth Management
Name: BriAnne Dockery
Title: Executive Assistant
Cell: (281) 555-0173
Direct Line: (832) 555-0148
Email: brianne@harborwmx.com
Address: 20537 W. Marlowe PKWY Ste. B
Tomball, TX 77390

I have attached the logo.
I would like it in navy blue and silver.
Thanks.

```html
<!DOCTYPE html>
<html lang="en">
<head>
<meta charset="UTF-8">
<title>Harbor Wealth Management – BriAnne Dockery</title>
<link rel="stylesheet" href="https://fonts.googleapis.com/css2?family=Marcellus&family=Arimo:wght@400&display=swap">
<style>
  :root {
    --navy: #14213d;
    --slate: #3c4660;
    --silver: #a7a8ac;
    --paper: #ffffff;
  }
  html, body {
    margin: 0;
    padding: 0;
    width: 960px;
    height: 1200px;
    overflow: hidden;
    background: var(--paper);
  }
  .card {
    position: relative;
    width: 960px;
    height: 1200px;
    background: var(--paper);
    overflow: hidden;
  }
  .silver-wedge {
    position: absolute;
    left: 0;
    top: 0;
  }
  .brand-mark {
    position: absolute;
    left: 419px;
    top: 150px;
    width: 150px;
    height: 150px;
    border-radius: 50%;
    background: var(--navy);
  }
  .brand-name {
    position: absolute;
    left: 0;
    top: 370px;
    width: 988px;
    margin: 0;
    text-align: center;
    font-family: "Marcellus", serif;
    font-weight: 400;
    font-size: 44px;
    line-height: 1;
    color: var(--navy);
  }
  .contact-name {
    position: absolute;
    left: 60px;
    top: 728px;
    margin: 0;
    font-family: "Marcellus", serif;
    font-weight: 400;
    font-size: 38px;
    line-height: 1;
    color: var(--navy);
    letter-spacing: 0.01em;
  }
  .contact-title {
    position: absolute;
    left: 60px;
    top: 786px;
    margin: 0;
    font-family: "Arimo", sans-serif;
    font-size: 33px;
    line-height: 1;
    color: var(--slate);
  }
  .title-rule {
    position: absolute;
    left: 60px;
    top: 826px;
    width: 147px;
    height: 3px;
    background: var(--navy);
  }
  .detail {
    position: absolute;
    left: 60px;
    margin: 0;
    font-family: "Arimo", sans-serif;
    font-size: 33px;
    line-height: 1;
    color: var(--slate);
    white-space: nowrap;
  }
  .detail-cell { top: 869px; }
  .detail-direct { top: 910px; }
  .detail-email { top: 976px; }
  .detail-street { top: 1055px; }
  .detail-city { top: 1101px; }
</style>
</head>
<body>
  <main class="card">
    <svg class="silver-wedge" width="960" height="1200" viewBox="0 0 960 1200" aria-hidden="true">
      <polygon points="427,626 960,626 960,1186" fill="var(--silver)"/>
    </svg>

    <div class="brand-mark" aria-hidden="true"></div>
    <p class="brand-name">Harbor Wealth Management</p>

    <h1 class="contact-name">BRIANNE DOCKERY</h1>
    <p class="contact-title">Executive Assistant</p>
    <div class="title-rule"></div>

    <p class="detail detail-cell">Cell: (281) 555–0173</p>
    <p class="detail detail-direct">Direct Line: (832) 555–0148</p>
    <p class="detail detail-email">brianne@harborwmx.com</p>
    <p class="detail detail-street">20537 W. Marlowe PKWY Ste. B</p>
    <p class="detail detail-city">Tomball, TX 77390.</p>
  </main>
</body>
</html>
```